Ridgewell Stonecraft Construction Needs business card

Hey we are in need of business card designs. I have upload our logo as a guideline, but free feel to run with it or come up with something unique.
Pls have fun with it and be creative. the name says it all!
i will give some directions after i see a few entries..
Logo source file has been uploaded..
Hey because of the logo is so colourful already.
Can we have a few submissions with less colour.
Also we are looking for clever/hidden/descriptive business card.

```html
<!DOCTYPE html>
<html lang="en">
<head>
<meta charset="utf-8">
<title>Ridgewell Stonecraft Construction – Business Card</title>
<link rel="stylesheet" href="https://fonts.googleapis.com/css2?family=Roboto:wght@400;700&display=swap">
<style>
  :root {
    --backdrop: #e4e4e6;
    --card-white: #f7f7f7;
    --pattern-grey: #e3e3e3;
    --accent-yellow: #e3e22f;
    --accent-red: #d8262b;
    --ink-grey: #6f6f72;
    --ink-dark: #4a4a4d;
    --name-blue: #2e7fc1;
    --rule-blue: #2a6fb0;
    --text-light: #ffffff;
  }
  * { box-sizing: border-box; margin: 0; padding: 0; }
  html, body {
    width: 1200px; height: 750px; overflow: hidden;
    background: var(--backdrop);
    font-family: "Roboto", Arial, sans-serif;
  }
  .stage {
    position: relative; width: 1200px; height: 750px;
    display: flex; align-items: center; justify-content: center; gap: 60px;
  }
  .card {
    position: relative; width: 460px; height: 264px;
    border-radius: 18px; overflow: hidden;
    background: var(--card-white);
    box-shadow: 0 6px 16px rgba(0,0,0,0.18);
  }
  .card-art { position: absolute; inset: 0; width: 100%; height: 100%; }
  .texture-field {
    position: absolute; border-radius: 6px;
    background: linear-gradient(135deg, var(--pattern-grey), rgba(227,227,227,0));
    opacity: 0.7;
  }
  .front .texture-field { left: 10px; top: 100px; width: 300px; height: 150px; }
  .back .texture-field { left: 80px; top: 20px; width: 300px; height: 200px; }

  .front-brand {
    position: absolute; left: 62px; top: 52px;
    display: flex; flex-direction: column; align-items: flex-end; gap: 4px;
  }
  .wordmark { display: flex; align-items: center; gap: 10px; }
  .wordmark-square { width: 18px; height: 18px; background: var(--ink-grey); }
  .wordmark-name {
    font-weight: 700; font-size: 22px; letter-spacing: 0.5px; line-height: 1;
    color: var(--ink-grey); text-transform: uppercase; white-space: nowrap;
  }
  .wordmark-tagline {
    font-size: 9px; letter-spacing: 2px; color: var(--ink-grey);
  }

  .back-mark {
    position: absolute; left: 40px; top: 70px;
    display: flex; align-items: center; gap: 8px;
  }
  .back-mark .wordmark-name { font-size: 15px; }
  .back-mark .wordmark-square { width: 14px; height: 14px; }
  .back-rule {
    position: absolute; left: 40px; top: 100px; width: 150px; height: 2px;
    background: var(--rule-blue);
  }
  .person { position: absolute; left: 42px; top: 196px; }
  .person-name { font-weight: 700; font-size: 17px; color: var(--name-blue); }
  .person-role { font-size: 10px; letter-spacing: 1.5px; color: var(--ink-grey); text-transform: uppercase; }

  .contact-list {
    position: absolute; left: 300px; top: 92px; list-style: none;
    color: var(--text-light); font-size: 10.5px; line-height: 16px;
  }
  .contact-list li { display: flex; align-items: center; gap: 6px; white-space: nowrap; }
  .contact-list svg { width: 11px; height: 11px; flex: none; }
  .contact-list .indent { padding-left: 17px; }
</style>
</head>
<body>
<main class="stage">

  <section class="card front" aria-label="Business card front">
    <div class="texture-field" role="img" aria-label="Faint grey block texture"></div>
    <svg class="card-art" viewBox="0 0 460 264" aria-hidden="true">
      <path d="M0,212 C150,214 300,160 460,104 L460,264 L0,264 Z" fill="var(--accent-yellow)"/>
      <path d="M0,206 C150,208 300,154 460,97" fill="none" stroke="#ffffff" stroke-width="3"/>
      <path d="M0,201 C150,203 300,149 460,90" fill="none" stroke="var(--accent-red)" stroke-width="6"/>
    </svg>
    <div class="front-brand">
      <div class="wordmark">
        <span class="wordmark-square"></span>
        <span class="wordmark-name">Ridgewell Stonecraft</span>
      </div>
      <div class="wordmark-tagline">CONSTRUCTION</div>
    </div>
  </section>

  <section class="card back" aria-label="Business card back">
    <div class="texture-field" role="img" aria-label="Faint grey block texture"></div>
    <svg class="card-art" viewBox="0 0 460 264" aria-hidden="true">
      <path d="M175,264 C250,200 300,70 365,0 L460,0 L460,264 Z" fill="var(--accent-yellow)"/>
      <path d="M170,264 C245,200 295,70 360,0" fill="none" stroke="#ffffff" stroke-width="3"/>
      <path d="M162,264 C237,200 287,70 352,0" fill="none" stroke="var(--accent-red)" stroke-width="7"/>
    </svg>
    <div class="back-mark">
      <span class="wordmark-square"></span>
      <span class="wordmark-name">Ridgewell Stonecraft</span>
    </div>
    <div class="back-rule"></div>
    <div class="person">
      <div class="person-name">Your Name</div>
      <div class="person-role">Director</div>
    </div>
    <ul class="contact-list">
      <li><svg viewBox="0 0 12 12"><path d="M2 1h3l1 3-2 1a7 7 0 0 0 3 3l1-2 3 1v3c-6 0-9-3-9-9z" fill="#fff"/></svg>012 345 6789</li>
      <li><svg viewBox="0 0 12 12"><path d="M2 1h3l1 3-2 1a7 7 0 0 0 3 3l1-2 3 1v3c-6 0-9-3-9-9z" fill="#fff"/></svg>012 345 6790</li>
      <li><svg viewBox="0 0 12 12"><rect x="1" y="2.5" width="10" height="7" fill="none" stroke="#fff"/><path d="M1 3l5 3.5L11 3" fill="none" stroke="#fff"/></svg>info@ridgewellstone.com</li>
      <li><svg viewBox="0 0 12 12"><path d="M6 1a3.5 3.5 0 0 1 3.5 3.5C9.5 7 6 11 6 11S2.5 7 2.5 4.5A3.5 3.5 0 0 1 6 1z" fill="#fff"/></svg>14 Quarry Lane</li>
      <li class="indent">Ashford, State 10245</li>
    </ul>
  </section>

</main>
</body>
</html>
```